Plakat-Design für Vereinsfest
Zielgruppe
Unser Verein veranstaltet jedes Jahr im August das Vereinsfest 'Sonnwendtag', das in einem kleinen Wäldchen innerhalb des Heimatortes stattfindet. Am Samstag und Sonntag sorgen verschiedene Musikgruppen für Unterhaltung. Es soll ein Veranstaltungsplakat gestaltet werden, dass sich an die Vorgaben (siehe unten) hält und die Veranstaltung bewirbt.
Zielgruppe sind Bürger des Heimatortes.
Aufgabenstellung
Das Vereinslogo ist beigefügt und sollte prominent auf dem Plakat vertreten sein, Logo und Schriftzug können auch getrennt oder anders angeordnet werden. Der Veranstaltungstitel lautet "Sonnwendtag", es findet am 20. und 21. August "Am Hirtenstein" (Veranstaltungsort) statt.
Programmpunkte: Samstag: Musikalische Unterhaltung mit den Bachpfeifern; Sonntag: Musikalische Unterhaltung mit den Moorbachrabauken
Uhrzeiten sollten enthalten sein:
Beginn Samstag: ab 15 Uhr
Beginn Sonntag: ab 10 Uhr
Das Plakat soll gut leserlich auch aus der Entfernung sein, da es an Straßen plakatiert wird.
Das Plakat soll für spätere Jahre editierbar sein.
Schriftart im Logo: Californian FB Bold (muss aber nicht auf andere Textelemente angewendet werden). Das Plakat soll in DIN A2 gedruckt werden. Die Webadresse sollte auf dem Plakat stehen.

```html
<!DOCTYPE html>
<html lang="de">
<head>
<meta charset="utf-8">
<title>Sonnwendtag – Plakat</title>
<link href="https://fonts.googleapis.com/css2?family=Cinzel:wght@500;700&family=Noto+Serif:wght@400;700&display=swap" rel="stylesheet">
<style>
  :root {
    --paper: #f6ece0;
    --paper-edge: #efe2d2;
    --frame-line: #b9aea3;
    --ornament: #e3d8cc;
    --brown: #8b4a12;
    --blue: #18689b;
    --olive: #a58f3e;
    --rust: #a6542f;
    --dark-brown: #6a3414;
    --crowd: #a7a39d;
    --ink: #3b2f2a;
    --white: #ffffff;
  }
  * { box-sizing: border-box; margin: 0; padding: 0; }
  html, body { width: 976px; height: 1200px; overflow: hidden; }
  body {
    position: relative;
    background: var(--paper);
    font-family: "Noto Serif", Georgia, serif;
    color: var(--ink);
  }
  .poster-frame {
    position: absolute; inset: 16px;
    border: 2px solid var(--frame-line);
  }
  .poster-frame::after {
    content: ""; position: absolute; inset: 6px;
    border: 1px solid var(--frame-line);
  }
  .corner {
    position: absolute; width: 110px; height: 110px;
    background: var(--ornament);
  }
  .corner--tl { top: 30px; left: 30px; border-radius: 0 0 100% 0; }
  .corner--tr { top: 30px; right: 30px; border-radius: 0 0 0 100%; }
  .corner--bl { bottom: 30px; left: 30px; border-radius: 0 100% 0 0; }
  .corner--br { bottom: 30px; right: 30px; border-radius: 100% 0 0 0; }

  .club {
    position: absolute; top: 52px; left: 0; right: 0;
    display: flex; justify-content: center; align-items: center; gap: 26px;
  }
  .club__mark {
    width: 104px; height: 104px; border-radius: 50%;
    background: #c9b5ab;
  }
  .club__name {
    font-weight: 400; font-size: 30px; line-height: 1.05;
    color: var(--ink);
  }

  .title {
    position: absolute; top: 268px; left: 0; right: 0;
    text-align: center;
  }
  .title__rule { display: block; margin: 0 auto; height: 3px; }
  .title__rule--top { width: 330px; background: var(--olive); margin-bottom: 2px; }
  .title__word {
    font-family: "Cinzel", "Times New Roman", serif;
    font-weight: 500; font-size: 82px; line-height: 1;
    letter-spacing: -1px; white-space: nowrap; display: block;
    padding: 6px 0 8px;
  }
  .title__word .cap { font-size: 110px; }
  .title__rule--bottom-a { width: 800px; background: var(--rust); margin-bottom: 6px; }
  .title__rule--bottom-b { width: 800px; background: var(--olive); }

  .band {
    position: absolute; left: 50%; transform: translateX(-50%);
    color: var(--white); text-align: center; width: 560px;
  }
  .band--date { top: 470px; height: 96px; background: var(--blue); padding-top: 4px; }
  .band__date { font-weight: 700; font-size: 48px; line-height: 1.05; }
  .band__place { font-size: 38px; line-height: 1.05; }
  .band--programme { top: 580px; height: 134px; background: var(--olive); padding-top: 10px; }
  .programme__day { color: var(--ink); font-weight: 700; font-size: 19px; line-height: 1.15; }
  .programme__act { font-size: 16px; line-height: 1.2; margin-bottom: 6px; }
  .band--times { top: 728px; height: 76px; background: var(--rust); font-size: 26px; line-height: 1.3; padding-top: 5px; }

  .illustration { position: absolute; }
  .illustration--notes-left {
    top: 700px; left: 130px; width: 70px; height: 150px; border-radius: 35px;
    background: var(--olive); opacity: .35;
  }
  .illustration--notes-right {
    top: 716px; right: 130px; width: 70px; height: 170px; border-radius: 35px;
    background: var(--brown); opacity: .3;
  }
  .illustration--band {
    top: 830px; left: 250px; width: 476px; height: 160px; border-radius: 8px;
    background: linear-gradient(90deg, var(--brown) 0 14%, var(--olive) 14% 28%, var(--blue) 28% 43%, var(--rust) 43% 57%, var(--rust) 57% 71%, var(--blue) 71% 86%, var(--dark-brown) 86% 100%);
    opacity: .85;
  }
  .web {
    position: absolute; top: 1002px; left: 0; right: 0;
    text-align: center; font-size: 22px; font-weight: 700; color: var(--ink);
  }
  .illustration--crowd {
    top: 1046px; left: 290px; width: 396px; height: 112px;
    background: var(--crowd); opacity: .8;
  }
</style>
</head>
<body>
  <div class="poster-frame"></div>
  <div class="corner corner--tl" role="img" aria-label="Verschnörkeltes Eckornament"></div>
  <div class="corner corner--tr" role="img" aria-label="Verschnörkeltes Eckornament"></div>
  <div class="corner corner--bl" role="img" aria-label="Verschnörkeltes Eckornament"></div>
  <div class="corner corner--br" role="img" aria-label="Verschnörkeltes Eckornament"></div>

  <header class="club">
    <div class="club__mark"></div>
    <p class="club__name">Historischer<br>Heimatverein<br>Tannfeld e.V.</p>
  </header>

  <h1 class="title">
    <span class="title__rule title__rule--top"></span>
    <span class="title__word"><span class="cap" style="color:var(--brown)">S</span><span style="color:var(--blue)">O</span><span style="color:var(--olive)">N</span><span style="color:var(--rust)">N</span><span style="color:var(--blue)">W</span><span style="color:var(--olive)">E</span><span style="color:var(--dark-brown)">N</span><span style="color:var(--rust)">D</span><span style="color:var(--blue)">T</span><span style="color:var(--olive)">A</span><span class="cap" style="color:var(--rust)">G</span></span>
    <span class="title__rule title__rule--bottom-a"></span>
    <span class="title__rule title__rule--bottom-b"></span>
  </h1>

  <section class="band band--date">
    <p class="band__date">20 - 21 August</p>
    <p class="band__place">„Am Hirtenstein“</p>
  </section>

  <section class="band band--programme">
    <p class="programme__day">Samstag:</p>
    <p class="programme__act">Musikalische Unterhaltung mit den<br>Bachpfeifern</p>
    <p class="programme__day">Sonntag:</p>
    <p class="programme__act">Musikalische Unterhaltung<br>mit den Moorbachrabauken</p>
  </section>

  <section class="band band--times">
    <p>Beginn Samstag: ab 15 Uhr</p>
    <p>Beginn Sonntag: ab 10 Uhr</p>
  </section>

  <div class="illustration illustration--notes-left" role="img" aria-label="Notenschlüssel mit geschwungener Notenlinie"></div>
  <div class="illustration illustration--notes-right" role="img" aria-label="Geschwungene Notenlinie mit Noten"></div>
  <div class="illustration illustration--band" role="img" aria-label="Farbige Silhouetten einer Blaskapelle mit Saxofon, Trompeten, Tuba und Flöte"></div>
  <p class="web">www.heimatverein-tannfeld.de</p>
  <div class="illustration illustration--crowd" role="img" aria-label="Graue Silhouetten jubelnder Zuschauer"></div>
</body>
</html>
```